R&T Builders and Spaces Business Card

We need to redesign our business card. We had used white vellum wih grey logo and txt in the past. I would like to bring a little life into our cards without being over the top. I think I will be going away from the vellum and printing soft touch business cards.
I have attached what we currently have and our new logo design.

```html
<!DOCTYPE html>
<html lang="en">
<head>
<meta charset="utf-8">
<title>R&amp;T Builders and Spaces — Business Card</title>
<link href="https://fonts.googleapis.com/css2?family=Didact+Gothic&display=swap" rel="stylesheet">
<style>
  :root {
    --backdrop: #2b2b2b;
    --card: #3d3d3d;
    --ink: #ffffff;
    --panel: #bdbdbd;
  }
  html, body {
    margin: 0;
    padding: 0;
    width: 1200px;
    height: 900px;
    overflow: hidden;
    background: var(--backdrop);
    font-family: "Didact Gothic", "Century Gothic", sans-serif;
    color: var(--ink);
  }
  .canvas {
    position: relative;
    width: 1200px;
    height: 900px;
  }
  .card {
    position: absolute;
    top: 301px;
    width: 513px;
    height: 296px;
    background: var(--card);
    box-shadow: 0 4px 10px rgba(0,0,0,0.45);
  }
  .card--front { left: 73px; }
  .card--back { left: 615px; }

  .contact {
    position: absolute;
    left: 36px;
    top: 32px;
    line-height: 1.2;
  }
  .contact__name {
    font-size: 17px;
    letter-spacing: 0.5px;
    margin: 0;
  }
  .contact__title {
    font-size: 13px;
    margin: 2px 0 17px;
  }
  .contact__line {
    font-size: 13.5px;
    margin: 0;
  }
  .address {
    position: absolute;
    left: 36px;
    top: 239px;
    font-size: 14px;
    line-height: 1.3;
    margin: 0;
  }

  .brand {
    position: absolute;
    left: 374px;
    top: 160px;
    width: 91px;
    height: 91px;
  }
  .brand__square {
    width: 91px;
    height: 91px;
    background: var(--ink);
  }
  .brand__name,
  .brand__tagline {
    position: absolute;
    font-size: 8px;
    letter-spacing: 1.6px;
    white-space: nowrap;
    color: var(--ink);
  }
  .brand__name {
    left: 0;
    top: 95px;
  }
  .brand__tagline {
    left: 97px;
    top: 103px;
    transform: rotate(-90deg);
    transform-origin: 0 0;
  }

  .back-panel {
    position: absolute;
    left: 177px;
    top: 57px;
    width: 161px;
    height: 182px;
    background: var(--panel);
  }
  .website {
    position: absolute;
    left: 0;
    right: 0;
    top: 136px;
    text-align: center;
    font-size: 19px;
    letter-spacing: 0.3px;
    margin: 0;
  }
</style>
</head>
<body>
  <main class="canvas">
    <section class="card card--front" aria-label="Business card front">
      <div class="contact">
        <p class="contact__name">DANA M. WHITLOCK</p>
        <p class="contact__title">PRINCIPAL</p>
        <p class="contact__line">danaw@rtbuilders.com</p>
        <p class="contact__line">T 555 014 2730&nbsp; C 555 018 4462</p>
      </div>
      <p class="address">1840 W Harbor Rd, Suite 200<br>Fairview, Oregon 97024</p>
      <div class="brand">
        <div class="brand__square"></div>
        <span class="brand__name">R&amp;T BUILDERS</span>
        <span class="brand__tagline">AND SPACES</span>
      </div>
    </section>

    <section class="card card--back" aria-label="Business card back">
      <div class="back-panel"></div>
      <p class="website">WWW.RTBUILDERS.COM</p>
    </section>
  </main>
</body>
</html>
```